Business Card for Restaurant Nuvelo

This project consist of creating 2 design for business card of restaurant named Nuvelo.

The attached specs below are 'ONLY SUGGESTION' if you have others ideas. You are welcome to post it.

1) Restaurant Card

Adresse:
2318 Rue des Pruniers
Montréal (Qc) H3K 2T8

Website:
www.nu-velo.ca

Phone:
438-552-0194

2) Employee Card

Name: Greta Lund
Title: Owner

Address:
2318 Rue des Pruniers
Montréal (Qc) H3K 2T8

Email:greta@nu-velo.ca
Phone Number:438-552-0194
Cellphone Number:514-730-4816

 The attached specs are 'ONLY SUGGESTION' if you have others ideas.  You are welcome to post it.

Industry/Entity Type

Restaurant

Requirements
Must have
• UV Card Spot

To print Spot UV business cards you would have to submit 2 files for each side. The first file "base" would be your regular design file as it would have been in any other case. The 2nd file "UV mask" is a black/white file. The BLACK color will indicate the areas that will be covered with the UV high gloss finish. To upload the files, please combine front design and front mask file in one P
Nice to have
• 1) The font of the logo should be ink effect
2) black background with wallpaper effect
3) The specs below are 'ONLY SUGGESTION' if you have others ideas. You are welcome to post it.

```html
<!DOCTYPE html>
<html lang="fr">
<head>
<meta charset="utf-8">
<title>Nuvelo – Business Cards</title>
<link rel="stylesheet" href="https://fonts.googleapis.com/css2?family=Questrial&family=Inter:wght@400&display=swap">
<style>
  :root {
    --sheet: #cfcfcf;
    --label: #1e1e1e;
    --card-dark: #2a2828;
    --card-light: #d6d0c7;
    --ink-light: #ffffff;
    --ink-dark: #231f20;
    --accent: #e3262b;
    --motif-dark: rgba(255,255,255,0.22);
    --motif-light: rgba(255,255,255,0.45);
  }
  * { margin: 0; padding: 0; box-sizing: border-box; }
  html, body { width: 1200px; height: 1012px; overflow: hidden; }
  body {
    background: radial-gradient(ellipse at 50% 45%, #dcdcdc 0%, var(--sheet) 60%, #bdbdbd 100%);
    font-family: "Questrial", sans-serif;
    position: relative;
  }
  .label {
    position: absolute;
    font-family: "Inter", Arial, sans-serif;
    font-size: 16px;
    color: var(--label);
    transform: translateX(-50%);
    white-space: nowrap;
  }
  .card {
    position: absolute;
    width: 392px;
    height: 221px;
    overflow: hidden;
    box-shadow: 0 10px 14px -6px rgba(0,0,0,0.45);
  }
  .card--dark { background: var(--card-dark); color: var(--ink-light); }
  .card--light { background: var(--card-light); color: var(--ink-dark); }
  .motif {
    position: absolute;
    top: 0; bottom: 0;
    width: 180px;
    border-radius: 50% 40% 30% 45%;
  }
  .card--dark .motif { background: radial-gradient(ellipse at 40% 40%, var(--motif-dark), rgba(255,255,255,0.08) 75%); }
  .card--light .motif { background: radial-gradient(ellipse at 40% 40%, var(--motif-light), rgba(255,255,255,0.15) 75%); }
  .brand { position: absolute; display: flex; align-items: center; gap: 6px; white-space: nowrap; }
  .brand__name { line-height: 1; }
  .brand__dot { border-radius: 50%; background: var(--accent); flex: none; }
  .tagline { position: absolute; font-size: 5px; white-space: nowrap; }
  .tagline--large { font-size: 10px; }
  .tagline .sep { color: var(--accent); }
  .details { position: absolute; font-size: 9px; line-height: 1; }
  .details p { position: absolute; white-space: nowrap; display: flex; align-items: center; gap: 4px; }
  .details strong { font-weight: 400; letter-spacing: 0.2px; }
  .icon { width: 9px; height: 9px; flex: none; }
  .spot-note { position: absolute; left: 920px; top: 194px; }
  .spot-note span { position: absolute; left: 24px; top: 0; font-family: "Inter", Arial, sans-serif; font-size: 13px; color: var(--label); white-space: nowrap; }
  .size-note { position: absolute; left: 886px; top: 885px; font-family: "Inter", Arial, sans-serif; font-size: 13px; color: var(--label); }
</style>
</head>
<body>
  <div class="label" style="left:389px;top:180px;">Restaurant card</div>
  <div class="label" style="left:820px;top:180px;">Employee card</div>

  <div class="spot-note">
    <svg width="26" height="34" viewBox="0 0 26 34"><path d="M3 33 C1 22 6 14 18 10" fill="none" stroke="#333" stroke-width="1"/><path d="M13 7 L19 10 L14 14" fill="none" stroke="#333" stroke-width="1"/></svg>
    <span>Spot UV</span>
  </div>

  <!-- Restaurant card front -->
  <section class="card card--dark" style="left:190px;top:222px;">
    <div class="motif" role="img" aria-label="Large faint brush-ink motif in spot UV" style="left:205px;"></div>
    <div class="brand" style="left:34px;top:53px;">
      <span class="brand__name" style="font-size:30px;">Nuvelo</span>
      <span class="brand__dot" style="width:15px;height:15px;"></span>
    </div>
    <div class="tagline" style="left:40px;top:93px;">Resto-Bar Japonais <span class="sep">·</span> Izakaya <span class="sep">·</span> 居酒屋</div>
    <div class="details" style="left:35px;top:0;">
      <p style="top:113px;">2318 Rue des Pruniers</p>
      <p style="top:125px;">Montréal (Qc) H3K 2T8</p>
      <p style="top:142px;"><svg class="icon" viewBox="0 0 10 10"><circle cx="5" cy="5" r="4.4" fill="none" stroke="currentColor" stroke-width="0.8"/><path d="M3.5 3 Q3 6 6.5 7" fill="none" stroke="currentColor" stroke-width="1.2"/></svg>438-552-0194</p>
      <p style="top:158px;"><svg class="icon" viewBox="0 0 10 10"><circle cx="5" cy="5" r="4.4" fill="none" stroke="currentColor" stroke-width="0.8"/><ellipse cx="5" cy="5" rx="2" ry="4.4" fill="none" stroke="currentColor" stroke-width="0.8"/><path d="M0.6 5 H9.4" stroke="currentColor" stroke-width="0.8"/></svg>www.nu-velo.ca</p>
    </div>
  </section>

  <!-- Employee card front -->
  <section class="card card--light" style="left:626px;top:221px;">
    <div class="motif" role="img" aria-label="Large faint brush-ink motif in spot UV" style="left:198px;"></div>
    <div class="details" style="left:43px;top:0;">
      <p style="top:54px;">Owner</p>
      <p style="top:66px;"><strong>Greta Lund</strong></p>
      <p style="top:85px;"><svg class="icon" viewBox="0 0 10 10"><circle cx="5" cy="5" r="4.4" fill="none" stroke="currentColor" stroke-width="0.8"/><path d="M3.5 3 Q3 6 6.5 7" fill="none" stroke="currentColor" stroke-width="1.2"/></svg>438-552-0194</p>
      <p style="top:99px;"><svg class="icon" viewBox="0 0 10 10"><circle cx="5" cy="5" r="4.4" fill="none" stroke="currentColor" stroke-width="0.8"/><rect x="3.5" y="2.5" width="3" height="5" rx="0.6" fill="none" stroke="currentColor" stroke-width="0.8"/></svg>514-730-4816</p>
      <p style="top:112px;"><svg class="icon" viewBox="0 0 10 10"><circle cx="5" cy="5" r="4.4" fill="none" stroke="currentColor" stroke-width="0.8"/><ellipse cx="5" cy="5" rx="2" ry="4.4" fill="none" stroke="currentColor" stroke-width="0.8"/><path d="M0.6 5 H9.4" stroke="currentColor" stroke-width="0.8"/></svg>www.nu-velo.ca</p>
      <p style="top:125px;"><svg class="icon" viewBox="0 0 10 10"><rect x="0.5" y="2" width="9" height="6" fill="currentColor"/><path d="M0.5 2 L5 5.5 L9.5 2" fill="none" stroke="#d6d0c7" stroke-width="0.8"/></svg>greta@nu-velo.ca</p>
      <p style="top:147px;">2318 Rue des Pruniers</p>
      <p style="top:158px;">Montréal (Qc) H3K 2T8</p>
    </div>
    <div class="brand" style="left:222px;top:87px;">
      <span class="brand__name" style="font-size:30px;">Nuvelo</span>
      <span class="brand__dot" style="width:15px;height:15px;"></span>
    </div>
    <div class="tagline" style="left:228px;top:124px;">Resto-Bar Japonais <span class="sep">·</span> Izakaya <span class="sep">·</span> 居酒屋</div>
  </section>

  <div class="label" style="left:393px;top:465px;">Front</div>
  <div class="label" style="left:819px;top:465px;">Front</div>

  <!-- Restaurant card back -->
  <section class="card card--dark" style="left:190px;top:524px;">
    <div class="brand" style="left:90px;top:78px;">
      <span class="brand__name" style="font-size:54px;">Nuvelo</span>
      <span class="brand__dot" style="width:32px;height:32px;margin-top:30px;"></span>
    </div>
    <div class="tagline tagline--large" style="left:97px;top:146px;">Resto-Bar Japonais <span class="sep">·</span> Izakaya <span class="sep">·</span> 居酒屋</div>
  </section>

  <!-- Employee card back -->
  <section class="card card--light" style="left:624px;top:522px;">
    <div class="brand" style="left:86px;top:78px;">
      <span class="brand__name" style="font-size:54px;">Nuvelo</span>
      <span class="brand__dot" style="width:32px;height:32px;margin-top:30px;"></span>
    </div>
    <div class="tagline tagline--large" style="left:97px;top:146px;">Resto-Bar Japonais <span class="sep">·</span> Izakaya <span class="sep">·</span> 居酒屋</div>
  </section>

  <div class="label" style="left:393px;top:772px;">Back</div>
  <div class="label" style="left:819px;top:772px;">Back</div>

  <div class="size-note">Size : 90mm x 50mm</div>
</body>
</html>
```